Tree Pruning Website

We need a website for a tree Arborist, pruning company called Hollow Ridge Groundcare. We look after all types of trees, knock down trees and prune trees. Our target market is from domestic clients to government clients and everything in between.

We would like to see the use of our main colours which are orange and green

We are not looking forward in seeing a template that we have seen before but a unique template. We have designed 5 templates ourselves and we wish for the design community to take our designs to the next level.

We have also designed a template for things that **we are not** looking for (Version 4)

To make it fair for everyone, we are also not giving out any participation payments as we have had. One winner will take all of the payment!!!

I Have attached a image of the designs and a image of a tree.

We are just looking at the PSD file been developed. We have our own team who can slice the image up into a HTML format.

Target Market(s)

Everyone who needs to cut down a tree

Industry/Entity Type

Government

Requirements
Must have
• Logo on front page
A List of our services
jQuery slider on page
Phone Number on every page

```html
<!DOCTYPE html>
<html lang="en">
<head>
<meta charset="utf-8">
<title>Hollow Ridge Groundcare</title>
<link href="https://fonts.googleapis.com/css2?family=Arvo:wght@400;700&family=Open+Sans:ital,wght@0,300;0,400;0,600;0,700;1,400&display=swap" rel="stylesheet">
<style>
:root{
  --green:#727d0a;
  --green-dark:#5d6708;
  --green-light:#9aab1a;
  --lime:#a6b81c;
  --orange:#f0a30a;
  --orange-deep:#e08a00;
  --text:#555;
  --muted:#888;
  --grey-bg:#edeef0;
  --footer:#3c3c3c;
  --footer-bottom:#2c2c2c;
  --white:#fff;
}
*{margin:0;padding:0;box-sizing:border-box}
html,body{width:924px;height:1200px;overflow:hidden;background:var(--white)}
body{position:relative;font-family:"Open Sans",Arial,sans-serif;color:var(--text);font-size:6px}
.abs{position:absolute}
.header{left:0;top:0;width:924px;height:328px;background:var(--green)}
.brand{left:236px;top:30px;display:flex;align-items:center;gap:8px}
.brand-dot{width:22px;height:22px;border-radius:50%;background:#c9d23a}
.brand-name{font-family:"Arvo",serif;font-weight:700;font-size:15px;line-height:16px;color:var(--orange)}
.nav{left:424px;top:70px;display:flex;gap:15px;font-size:7.2px;color:var(--white)}
.nav span{padding-bottom:7px}
.nav .active{border-bottom:3px solid var(--orange)}
.slider{left:236px;top:100px;width:452px;height:227px;border:2px solid var(--green-light);background:linear-gradient(160deg,#6d8fb0 0%,#8a9c4a 30%,#a36a2c 60%,#6e4a26 100%)}
.arrow{width:26px;height:26px;border:2px solid var(--orange);border-radius:50%;top:180px}
.dots{left:441px;top:312px;display:flex;gap:5px}
.dots i{width:10px;height:10px;border-radius:50%;border:2px solid var(--white);background:#555}
.dots i:first-child{background:var(--green)}
.band{left:0;top:328px;width:924px;height:58px;background:var(--orange)}
.band-shadow{left:30px;top:386px;width:864px;height:26px;background:radial-gradient(ellipse at top,rgba(0,0,0,.22),rgba(0,0,0,0) 70%)}
.band-text{left:244px;top:337px;width:296px;font-size:10.2px;font-weight:300;line-height:14px;color:var(--white)}
.band-text b{color:#3b3200;font-weight:700}
.phone-box{left:539px;top:328px;width:385px;height:58px;background:linear-gradient(90deg,var(--orange-deep),#ffb400)}
.phone-icon{left:549px;top:343px;width:30px;height:30px;border-radius:50%;background:var(--green);border:2px solid #d8d26b}
.phone-num{left:589px;top:345px;font-size:17px;color:var(--white)}
.ribbon{left:206px;top:432px}
.sector{top:488px;width:120px;text-align:center}
.sector h3{font-family:"Arvo",serif;font-weight:400;font-size:11px;color:#333;letter-spacing:.3px}
.sector p{margin-top:9px;font-size:6.3px;line-height:10px;color:var(--text)}
.btn{display:inline-block;background:var(--orange);color:var(--white);font-size:6.6px;font-weight:600;padding:4px 4px;border-radius:2px;margin-top:10px}
.section-title{font-family:"Arvo",serif;font-weight:400;font-size:10.5px;color:#333;white-space:nowrap}
.section-title.narrow{font-size:9.6px}
.rule{height:4px;background:var(--lime)}
.overview p{font-size:6.2px;line-height:8.8px;margin-bottom:8px}
.link{color:var(--lime)}
.why li{list-style:none;font-size:6.3px;color:var(--green);margin-bottom:10px;white-space:nowrap}
.why li::before{content:"→ ";color:var(--lime)}
.card{top:819px;width:106px;height:113px;background:var(--grey-bg)}
.card-img{width:106px;height:78px;border:3px solid var(--orange)}
.card h4{font-family:"Arvo",serif;font-weight:400;font-size:7.6px;color:#333;margin:7px 0 0 4px}
.card small{display:block;font-size:5.6px;color:var(--muted);margin-left:4px}
.feed{left:582px;top:819px;width:106px;height:113px;border:1px solid #ddd;background:#f7f7f7;padding:8px 8px;font-size:5px;line-height:6.6px;color:#444}
.feed p{margin-bottom:6px}
.feed em{font-style:normal;color:var(--green-light)}
.quote-band{left:0;top:954px;width:924px;height:49px;background:var(--grey-bg)}
.quote{left:288px;top:971px;width:286px;font-size:6.1px;line-height:8.5px;font-style:italic;color:#444}
.author{left:618px;top:977px;font-size:6.3px;color:#333}
.footer{left:0;top:1003px;width:924px;height:175px;background:var(--footer)}
.footer-bottom{left:0;top:1178px;width:924px;height:22px;background:var(--footer-bottom)}
.fcol{top:1028px}
.fcol h5{font-family:"Arvo",serif;font-weight:400;font-size:7.6px;color:var(--white);margin-bottom:12px}
.fcol p{font-size:5.2px;line-height:8.6px;color:#888}
.news p{border-bottom:1px solid #555;padding-bottom:6px;margin-bottom:6px}
.thumb{width:27px;height:27px;border:2px solid #eee}
.copyright{left:236px;top:1184px;font-size:5.4px;color:#999}
</style>
</head>
<body>
<header class="abs header">
  <div class="abs brand"><span class="brand-dot"></span><div class="brand-name">Hollow Ridge<br>Groundcare</div></div>
  <nav class="abs nav"><span class="active">Home</span><span>About Us</span><span>Our Services</span><span>Get A quote</span><span>Our Work</span><span>Contact Us</span></nav>
  <div class="abs slider" role="img" aria-label="Photo looking up a large tree trunk into a sunlit green and orange canopy"></div>
  <svg class="abs arrow" style="left:201px" viewBox="0 0 26 26"><path d="M18 13H8M12 8l-5 5 5 5" stroke="#fff" stroke-width="2.5" fill="none"/></svg>
  <svg class="abs arrow" style="left:698px" viewBox="0 0 26 26"><path d="M8 13h10M14 8l5 5-5 5" stroke="#fff" stroke-width="2.5" fill="none"/></svg>
  <div class="abs dots"><i></i><i></i><i></i></div>
</header>

<section class="abs band"></section>
<div class="abs band-shadow"></div>
<p class="abs band-text">Hollow Ridge is the leading tree pruning services located Perth. Our motto is when you call, we <b>guarantee</b> to turn up and <b>provide care</b> to our customers.</p>
<div class="abs phone-box"></div>
<svg class="abs phone-icon" viewBox="0 0 30 30"><path d="M10 8c1-1 2-1 3 0l1 3-2 2c1 2 3 4 5 5l2-2 3 1c1 1 1 2 0 3-2 2-5 2-8-1s-6-6-6-8 1-2 2-3z" fill="#fff"/></svg>
<div class="abs phone-num">08 5550 0142</div>

<svg class="abs ribbon" width="512" height="42" viewBox="0 0 512 42">
  <path d="M0 14h30v30H0l10-15z" fill="#5d6708" transform="translate(0,-2)"/>
  <path d="M512 14h-30v30h30l-10-15z" fill="#5d6708" transform="translate(0,-2)"/>
  <rect x="30" y="2" width="452" height="28" fill="#8a9b12"/>
  <g fill="#f0a30a" stroke="#fff" stroke-width="2">
    <circle cx="83" cy="16" r="14"/><circle cx="198" cy="16" r="14"/><circle cx="313" cy="16" r="14"/><circle cx="429" cy="16" r="14"/>
  </g>
  <g fill="#fff">
    <rect x="79" y="11" width="8" height="10" rx="1"/>
    <rect x="191" y="12" width="14" height="8" rx="1"/>
    <circle cx="313" cy="12" r="3"/><path d="M307 22c1-5 11-5 12 0z"/>
    <path d="M423 22c0-7 5-11 12-12-1 7-5 11-12 12z"/>
  </g>
</svg>

<div class="abs sector" style="left:229px"><h3>DOMESTIC</h3><p>At vero eos et accusam et justo duo dolores et ea rebum. Stet clita kasd gubergren, no sea takimata sanctus est Lorem ipsum dolor sit amet.</p><span class="btn">Learn more</span></div>
<div class="abs sector" style="left:344px"><h3>COMMERCIAL</h3><p>Ut wisi enim ad minim veniam, quis nostrud exerci tation ullamcorper suscipit lobortis nisl ut aliquip ex ea commodo consequat.</p><span class="btn">Learn more</span></div>
<div class="abs sector" style="left:459px"><h3>GOVERMENT</h3><p>Nam liber tempor cum soluta nobis eleifend option congue nihil imperdiet doming id quod mazim placerat facer possim assum.</p><span class="btn">Learn more</span></div>
<div class="abs sector" style="left:575px"><h3>NON PROFIT</h3><p>Lorem ipsum dolor sit amet, consetetur sadipscing elitr, sed diam nonumy eirmod tempor invidunt ut labore et dolore.</p><span class="btn">Learn more</span></div>

<div class="abs" style="left:236px;top:597px;width:337px;border-top:1px solid #e2e2e2;padding-top:6px"><h2 class="section-title">Company Overview</h2></div>
<div class="abs rule" style="left:236px;top:621px;width:337px"></div>
<div class="abs overview" style="left:236px;top:641px;width:322px">
  <p><span class="link">Duis autem vel eum iriure</span> dolor in hendrerit in vulputate velit esse molestie consequat, vel illum dolore eu feugiat nulla facilisis at vero eros et accumsan et iusto odio dignissim qui blandit praesent luptatum zzril delenit augue duis dolore te feugait nulla facilisi. Lorem ipsum dolor sit amet, consectetuer adipiscing elit, sed diam nonummy nibh euismod tincidunt ut laoreet dolore magna aliquam erat volutpat.</p>
  <p>Ut wisi enim ad minim veniam, quis nostrud exerci tation ullamcorper suscipit lobortis nisl ut <span class="link">aliquip ex ea commodo consequat</span>. Duis autem vel eum iriure dolor in hendrerit in vulputate velit esse molestie consequat, vel illum dolore eu feugiat nulla facilisis at vero eros et accumsan et iusto odio dignissim qui blandit praesent luptatum zzril delenit augue duis dolore te feugait nulla facilisi. Nam liber tempor cum soluta nobis eleifend option congue nihil imperdiet doming id quod mazim placerat facer possim assum. Lorem ipsum dolor sit amet.</p>
  <p class="link">Ut laoreet dolore magna aliquam erat volutpat. Ut wisi enim ad minim veniam, quis nostrud exerci tation ullamcorper suscipit lobortis nisl ut aliquip ex ea commodo consequat.</p>
</div>

<div class="abs" style="left:584px;top:597px;width:104px;border-top:1px solid #e2e2e2;padding-top:6px"><h2 class="section-title narrow">Why Hollow Ridge?</h2></div>
<div class="abs rule" style="left:584px;top:621px;width:104px"></div>
<ul class="abs why" style="left:584px;top:644px">
  <li>Doloor in hendrerit in vulputate</li><li>Velit esse molestie consequat</li><li>Vel illum dolore eu feugiat</li><li>Nulla facilisis at vero eros et</li><li>Accumsan et iusto odio dignissim</li><li>Qui blandit praesent luptatum zzr.</li>
</ul>

<div class="abs" style="left:236px;top:771px;width:337px;border-top:1px solid #e2e2e2;padding-top:6px"><h2 class="section-title">Our Services</h2></div>
<svg class="abs" style="left:544px;top:778px" width="30" height="12" viewBox="0 0 30 12"><circle cx="6" cy="6" r="5" fill="none" stroke="#ccc"/><circle cx="21" cy="6" r="5" fill="none" stroke="#ccc"/><path d="M8 6H4M6 4L4 6l2 2M19 6h4M21 4l2 2-2 2" stroke="#ccc" fill="none"/></svg>
<div class="abs rule" style="left:236px;top:795px;width:337px"></div>

<article class="abs card" style="left:236px"><div class="card-img" role="img" aria-label="Photo of pale eucalyptus branches against the sky" style="background:linear-gradient(160deg,#d9dde0,#8a8f86 60%,#5d6650)"></div><h4>Observation 1</h4><small>Locations</small></article>
<article class="abs card" style="left:352px"><div class="card-img" role="img" aria-label="Photo of a leafy tree canopy seen from below" style="background:linear-gradient(160deg,#9ccf4a,#3f6a1e 55%,#1d2a10)"></div><h4>Observation 1</h4><small>Locations</small></article>
<article class="abs card" style="left:467px"><div class="card-img" role="img" aria-label="Photo of a sunlit forest path" style="background:linear-gradient(180deg,#4f7a28,#c8c98a 55%,#6d6a38)"></div><h4>Observation 1</h4><small>Locations</small></article>

<div class="abs" style="left:584px;top:771px;width:104px;border-top:1px solid #e2e2e2;padding-top:6px;display:flex;align-items:center;gap:6px">
  <svg width="20" height="14" viewBox="0 0 20 14"><path d="M2 9c3 0 5-1 6-3 2 2 6 3 9 0 0-3-2-5-5-5S7 3 7 5C5 5 3 4 1 2c0 3 1 5 3 6z" fill="#444"/></svg>
  <h2 class="section-title">Social Feed</h2></div>
<div class="abs rule" style="left:584px;top:795px;width:104px"></div>
<div class="abs feed">
  <p><em>@hollowridgegc</em> Stet clita kasd gubergren, no sea takimata sanctus est Lorem ipsum....by <em>hollowridgegc</em><br>about 2 hour ago</p>
  <p><em>@hollowridgegc</em> Stet clita kasd gubergren, no sea takimata sanctus est Lorem ipsum....by <em>hollowridgegc</em><br>about 2 hour ago</p>
  <p><em>@hollowridgegc</em> Stet clita kasd gubergren, no sea takimata sanctus est Lorem ipsum....by <em>hollowridgegc</em><br>about 2 hour ago</p>
</div>

<section class="abs quote-band"></section>
<svg class="abs" style="left:457px;top:954px" width="10" height="50" viewBox="0 0 10 50"><rect width="10" height="8" fill="#a6b81c"/><rect y="42" width="10" height="8" fill="#a6b81c"/><path d="M2 5l3-3 3 3M2 45l3 3 3-3" stroke="#fff" fill="none"/></svg>
<svg class="abs" style="left:245px;top:966px" width="30" height="22" viewBox="0 0 30 22"><path d="M2 2h16v11H8l-4 4v-4H2z" fill="#333"/><path d="M20 6h8v10h-2v4l-4-4h-8v-1h6z" fill="#333"/></svg>
<p class="abs quote">“ Duis autem vel eum iriure dolor in hendrerit in feugiat nulla facilisis at vero eros et accumsan vulputate velit esse molestie consequat, vel illum dolore eu pasto. ”</p>
<div class="abs" style="left:588px;top:963px;width:1px;height:32px;background:#ccc"></div>
<svg class="abs" style="left:598px;top:975px" width="12" height="12" viewBox="0 0 12 12"><circle cx="6" cy="4" r="3" fill="#444"/><path d="M0 12c1-5 11-5 12 0z" fill="#444"/></svg>
<p class="abs author"><b>Mara Ellison</b> - Goverment -</p>

<footer class="abs footer"></footer>
<svg class="abs" style="left:242px;top:1003px" width="32" height="16" viewBox="0 0 32 16"><path d="M0 0h32L0 16z" fill="#edeef0"/></svg>
<div class="abs fcol" style="left:236px;width:100px"><h5>ABOUT US</h5><p>Lorem ipsum dolor sit amet, consetetur sadipscing elitr, sed diam nonumy eirmod tempor invidunt ut labore et dolore magna aliquyam erat, sed diam voluptua. At vero eos et accusam et justo duo dolores et ea rebum. Stet clita kasd gubergren, no sea takimata sanctus est Lorem ipsum dolor sit amet</p></div>
<div class="abs fcol news" style="left:351px;width:96px"><h5>LATEST NEWS</h5><p>Lorem ipsum dolor sit amet, consetetur sadipscing elitr, sed diam.</p><p style="color:#c3cd2a">Nonumy eirmod tempor invidunt ut.</p><p>Labore et dolore magna aliquyam erat, sed diam voluptua.</p><p>At vero eos et accusam et justo duo dolores et ea rebum.</p></div>
<div class="abs fcol" style="left:467px;width:110px"><h5>GALLERY</h5>
  <div style="display:grid;grid-template-columns:repeat(3,27px);gap:12px 13px">
    <div class="thumb" role="img" aria-label="Small photo of a seedling in a droplet" style="background:linear-gradient(#9fd3f0,#5a8a2a)"></div>
    <div class="thumb" role="img" aria-label="Small portrait photo" style="background:linear-gradient(#d9b48f,#6a8a3a)"></div>
    <div class="thumb" role="img" aria-label="Small photo of a river landscape" style="background:linear-gradient(#5aa060,#2c7d86)"></div>
    <div class="thumb" role="img" aria-label="Small photo of grass" style="background:linear-gradient(#e6f0c0,#6aa82a)"></div>
    <div class="thumb" role="img" aria-label="Small photo of a flower in a field" style="background:linear-gradient(#4d7a20,#b7c95a)"></div>
    <div class="thumb" role="img" aria-label="Small outdoor portrait photo" style="background:linear-gradient(#8ab46a,#d8b99a)"></div>
  </div>
  <span class="btn" style="margin:11px 0 0 60px;padding:4px 4px">more gallery</span>
</div>
<div class="abs fcol" style="left:585px;width:104px"><h5>GET IN TOUCH</h5>
  <div role="img" aria-label="Street map of the office location" style="width:104px;height:55px;border:2px solid #eee;background:linear-gradient(135deg,#e8eadf,#d6dcc8)"></div>
  <p style="margin-top:5px">14 Larkspur Lane<br>FERNVALE, WA 6071</p>
  <p style="margin-top:5px;color:#ddd">☎ 08 5550 0199<br>☎ 08 5550 0199<br><span style="color:#888">✉ hello@hollowridge.example</span></p>
</div>
<div class="abs footer-bottom"></div>
<p class="abs copyright">© Copyright 2013 Hollow Ridge Groundcare.</p>
<div class="abs" style="left:647px;top:1186px;display:flex;gap:10px"><i style="width:7px;height:7px;background:#777"></i><i style="width:7px;height:7px;background:#777;border-radius:50%"></i><i style="width:7px;height:7px;background:#777"></i></div>
</body>
</html>
```